Flyer-Design für Stillkissen
Zielgruppe
Verkauf von EPS-Perlen (Sitzsackfüllung) Stillkissen, Sitzsäcke
Aufgabenstellung
Din A5 oder Din A6
Design der Webseite, oder neues Design das sich leicht auf die Webseite übertragen lässt.
www.benoka.de

```html
<!DOCTYPE html>
<html lang="de">
<head>
<meta charset="utf-8">
<title>benoka – Stillkissen Flyer</title>
<link href="https://fonts.googleapis.com/css2?family=Lato:wght@300;400;700;900&display=swap" rel="stylesheet">
<style>
  :root {
    --backdrop: #e2dcda;
    --paper: #ffffff;
    --ink: #1b1b1d;
    --brand-blue: #3a7fc2;
    --deep-blue: #0a6db6;
    --mid-blue: #6190cc;
    --soft-blue: #9bb0dc;
    --pale-blue: #dfe6f6;
    --photo-tone-a: #efedf3;
    --photo-tone-b: #dcd8e2;
  }
  * { margin: 0; padding: 0; box-sizing: border-box; }
  html, body { width: 1200px; height: 883px; overflow: hidden; }
  body {
    background: var(--backdrop);
    font-family: "Lato", sans-serif;
    color: var(--ink);
    position: relative;
  }
  .flyer {
    position: absolute;
    top: 146px;
    width: 420px;
    height: 591px;
    background: var(--paper);
    overflow: hidden;
  }
  .flyer--front { left: 150px; }
  .flyer--back { left: 630px; }

  .product-photo {
    position: absolute;
    left: 16px; top: 16px;
    width: 387px; height: 303px;
    background: radial-gradient(ellipse at 50% 45%, var(--photo-tone-a) 0%, var(--photo-tone-b) 100%);
  }
  .product-title {
    position: absolute;
    left: 16px; top: 337px;
    font-size: 15.5px;
    font-weight: 900;
  }
  .copy {
    position: absolute;
    left: 16px;
    font-size: 9.6px;
    line-height: 12.7px;
    font-weight: 400;
  }
  .copy p + p { margin-top: 12.7px; }
  .flyer--front .copy { top: 370px; width: 320px; }
  .flyer--back .copy { top: 376px; width: 280px; }

  .material-table {
    position: absolute;
    left: 16px; top: 525px;
    font-size: 6.4px;
    line-height: 10px;
    border-collapse: collapse;
  }
  .material-table th { text-align: left; font-weight: 700; }
  .material-table td { padding: 0; }
  .material-table td:first-child { width: 61px; }

  .brand-name {
    position: absolute;
    top: 553px;
    display: flex;
    align-items: center;
    gap: 5px;
    font-size: 19px;
    font-weight: 300;
    color: var(--brand-blue);
    letter-spacing: 0.5px;
  }
  .brand-name::before {
    content: "";
    width: 8px; height: 8px;
    border: 1.3px solid var(--brand-blue);
    border-radius: 50%;
  }
  .flyer--front .brand-name { right: 18px; }
  .flyer--back .brand-name { left: 16px; }

  .bubbles {
    position: absolute;
    left: 0; top: 0;
    width: 420px; height: 591px;
  }
  .shop-callout {
    position: absolute;
    left: 250px; top: 520px;
    width: 150px;
    text-align: center;
    color: var(--paper);
    font-size: 8.8px;
    line-height: 11.5px;
    transform: rotate(-8deg);
  }
  .shop-callout strong { font-weight: 700; }
</style>
</head>
<body>

<section class="flyer flyer--front">
  <div class="product-photo" role="img" aria-label="Foto: weißes Stillkissen mit grauen und schwarzen Sternen, U-förmig liegend"></div>
  <h1 class="product-title">Stillkissen Weiß mit Sternen</h1>
  <div class="copy">
    <p>Schönes, weiches und anschmiegsames Stillkissen. Ideal während der Schwangerschaft und Stillzeit. Perfekter Begleiter für Mutter und Kind.</p>
    <p>Das Kissen mit Mikroperlen gefüllt, ist auch geeignet für alle, die es gern gemütlich haben wollen. Egal ob auf der Couch oder im Bett als Seiten­schläferkissen.</p>
    <p>Dieses Stillkissen ist gefüllt mit ca. 40 L 1-2 mm Purotest®-Zertifizierten EPS-Perlen von einem Deutschen Hersteller.</p>
  </div>
  <table class="material-table">
    <tr><th colspan="2">Material</th></tr>
    <tr><td>Hülle</td><td>100% Baumwolle</td></tr>
    <tr><td>Innenkissen</td><td>100% Baumwolle</td></tr>
    <tr><td>Füllung</td><td>100% Polystyrol (1-2 mm Purotest®)</td></tr>
    <tr><td>Länge</td><td>ca. 190cm</td></tr>
  </table>
  <div class="brand-name">benoka</div>
</section>

<section class="flyer flyer--back">
  <svg class="bubbles" viewBox="0 0 529 745" xmlns="http://www.w3.org/2000/svg">
    <circle cx="264" cy="4" r="60" fill="var(--pale-blue)"/>
    <circle cx="97" cy="81" r="82" fill="var(--soft-blue)"/>
    <circle cx="223" cy="207" r="127" fill="var(--soft-blue)"/>
    <circle cx="97" cy="81" r="60" fill="#3aa0d8" role="img" aria-label="Stoffmuster: türkis mit Blumen und Herzen"/>
    <circle cx="349" cy="289" r="85" fill="var(--deep-blue)"/>
    <circle cx="264" cy="212" r="62" fill="var(--brand-blue)"/>
    <circle cx="264" cy="212" r="59" fill="#d6ebf7" role="img" aria-label="Stoffmuster: hellblaue Punkte auf Weiß"/>
    <circle cx="454" cy="69" r="77" fill="var(--pale-blue)"/>
    <circle cx="454" cy="69" r="74" fill="#55575c" role="img" aria-label="Stoffmuster: grau mit türkisen Tropfen"/>
    <circle cx="506" cy="214" r="60" fill="var(--mid-blue)"/>
    <circle cx="61" cy="311" r="105" fill="#c8d3ee"/>
    <circle cx="61" cy="311" r="99" fill="#ffffff"/>
    <circle cx="61" cy="311" r="97" fill="#a3a2a8" role="img" aria-label="Foto: graues Stillkissen mit weißem Tropfenmuster"/>
    <circle cx="433" cy="379" r="77" fill="var(--pale-blue)"/>
    <circle cx="433" cy="379" r="60" fill="#cfe0ea" role="img" aria-label="Stoffmuster: blaue und grüne Blumen auf Weiß"/>
    <circle cx="413" cy="742" r="130" fill="var(--soft-blue)"/>
  </svg>
  <div class="copy">
    <p>Unsere Stillkissen gibt es in vielen Variationen. Wählen Sie Ihr Lieblingsdesign und machen Sie es sich gemütlich.</p>
    <p>Der Außenbezug ist abnehmbar und kann seperat gewaschen werden.</p>
  </div>
  <p class="shop-callout">Wählen Sie Ihr Lieblingsdesign im Onlineshop unter <strong>www.benoka.de</strong></p>
  <div class="brand-name">benoka</div>
</section>

</body>
</html>
```